Website Design: Neuroscience research lab at an academic University.

I am looking to redo my University website for Neuroscience Research. <br/><br/>I am looking for a clean, modern and organized design to publish our work. Although I want a modern look, the focus should be on the text content.<br/><br/>Pages I need. These pages should be in the navigation bar;<br/>*Home*: with overview of the lab, contact information, and possibly with <br/>"Recent News and Events" information<br/>*Research*/Projects: will have text description, images, as well as video of various research projects we have done or are working on<br/>*People*: Personnel page with photos and bios of the team<br/>*Publications*: List of research articles with hyperlinks to online <br/>versions of articles as well as PDFs<br/>*News*: Continually updated list of events<br/><br/><br/>Some designs I like: <br/><br/>https://www.morvanlabs.example/<br/>http://www.quillarbor.example/<br/>https://tenwicklab.example<br/>http://www.galdrenlab.example/<br/>https://vqom.halbrook.example/

Target Market(s)

Academics, university students, government

Logo Text

Pellory Lab

Number of Pages Required

5+ page

Colors

Designer to choose colors to be used in the design.

Requirements
Must have
• A modern but elegant design that focuses on the research but that is also visually appealing.
• For the logo, please see the sketch in the attached files. That is a rough sketch of a logo that you can base your logo design on.
Should not have
• No search bar

```html
<!DOCTYPE html>
<html lang="en">
<head>
<meta charset="utf-8">
<title>Our People – Neuroscience Research</title>
<link href="https://fonts.googleapis.com/css2?family=Montserrat:wght@300;400;500;600&display=swap" rel="stylesheet">
<style>
:root{
  --blue:#2f8ad9;
  --text:#555b63;
  --muted:#8a9097;
  --dark:#3b4047;
  --white:#ffffff;
  --line:#dcdfe2;
}
*{margin:0;padding:0;box-sizing:border-box}
html,body{width:756px;height:1200px;overflow:hidden}
body{font-family:'Montserrat',sans-serif;color:var(--text);background:var(--white);position:relative}
.abs{position:absolute}
/* hero */
.hero{left:0;top:0;width:756px;height:214px;overflow:hidden}
.hero-photo{position:absolute;inset:0;background:
  radial-gradient(ellipse 120px 90px at 690px 190px,rgba(201,120,40,.75),transparent 70%),
  radial-gradient(ellipse 260px 160px at 560px 80px,#4a6f8d,transparent 70%),
  linear-gradient(180deg,#0b2a45 0%,#1a4a70 55%,#2d5d82 100%)}
.brand{display:flex;align-items:center;gap:8px}
.brand-dot{width:46px;height:46px;border-radius:50%;background:#5e9ae0}
.brand-name{font-weight:300;font-size:11.5px;line-height:11.5px;letter-spacing:1.3px;text-transform:uppercase}
.hero .brand{left:76px;top:16px;color:var(--white)}
.nav{left:312px;top:33px;display:flex;font-size:7.4px;font-weight:500;color:var(--white)}
.nav a{color:inherit;text-decoration:none;margin-right:16.5px}
.btn-outline{border:1px solid var(--white);color:var(--white);font-size:7.4px;font-weight:500;display:flex;align-items:center;justify-content:center}
.hero .btn-outline{left:605px;top:27px;width:75px;height:21px}
.page-title{left:0;width:756px;top:120px;text-align:center;color:var(--white);font-weight:300;font-size:18px}
.title-rule{left:353px;top:148px;width:50px;height:1px;background:rgba(255,255,255,.8)}
/* people */
.person{left:0;width:756px}
.person.alt{background:linear-gradient(160deg,#eeeff1 0%,#fafafa 70%,#ffffff 100%)}
.portrait{position:absolute;left:96px;width:172px;height:153px}
.portrait.warm{background:radial-gradient(ellipse at 50% 45%,#8a6f5a 0%,#b8a07a 55%,rgba(184,160,122,0) 72%)}
.portrait.dark{background:radial-gradient(ellipse at 50% 45%,#5a3a2c 0%,#3a2e28 50%,rgba(127,164,212,.35) 64%,rgba(127,164,212,0) 74%)}
.portrait.grey{background:radial-gradient(ellipse at 50% 45%,#cdb8ab 0%,#c4c4c6 55%,rgba(196,196,198,0) 72%)}
.name{position:absolute;left:302px;font-size:12px;font-weight:500;color:var(--blue)}
.role{position:absolute;left:302px;font-size:7.4px;color:var(--muted)}
.contact{position:absolute;left:302px;font-size:7.4px;color:var(--text)}
.bio{position:absolute;left:302px;width:303px;font-size:7.4px;line-height:12.1px;text-align:justify;hyphens:auto;color:var(--text)}
.icon-btn{position:absolute;left:632px;width:20px;height:20px;border-radius:50%}
.icon-btn.solid{background:var(--blue)}
.icon-btn.ring{border:1px solid var(--blue);display:flex;align-items:center;justify-content:center}
/* band */
.cta{left:0;top:872px;width:756px;height:101px;background:var(--blue);color:var(--white)}
.cta h2{position:absolute;left:74px;top:32px;font-weight:300;font-size:18px}
.cta p{position:absolute;left:74px;top:55px;font-size:9.4px;font-weight:300}
.cta .btn-outline{left:529px;top:38px;width:151px;height:25px}
/* footer */
.footer{left:0;top:973px;width:756px;height:227px;background:linear-gradient(160deg,#f1f2f3,#fafafa 60%,#f3f4f5)}
.footer .brand{left:76px;top:38px;color:var(--dark)}
.footer .brand-dot{background:#6aa3e4}
.footer-rule{left:76px;top:91px;width:151px;height:1px;background:var(--line)}
.footer-art{left:76px;top:93px;width:151px;height:98px;background:linear-gradient(180deg,#ebedef,rgba(235,237,239,0))}
.quick{left:390px;top:52px;font-size:7.4px}
.quick h4{color:var(--blue);font-weight:600;font-size:7.4px;margin-bottom:9px}
.quick a{display:block;color:var(--text);text-decoration:none;margin-bottom:9.3px}
.call{right:76px;top:48px;text-align:right}
.call .phone{font-size:17px;font-weight:300;color:var(--dark)}
.call .mail{font-size:9.4px;font-weight:500;color:var(--dark);margin-top:2px}
.call .hours{font-size:5.5px;letter-spacing:1px;color:var(--muted);margin-top:8px}
.socials{right:76px;top:109px;display:flex;gap:6px}
.socials span{width:20px;height:20px;border-radius:50%;background:var(--blue);display:block}
.bottom-rule{left:25px;top:190px;width:706px;height:1px;background:var(--line)}
.copy{left:75px;top:205px;font-size:6px;color:var(--text)}
</style>
</head>
<body>

<header class="abs hero">
  <div class="hero-photo" role="img" aria-label="Blue-toned laboratory photo with pipette, glass beakers and microscope"></div>
  <div class="abs brand"><span class="brand-dot"></span><span class="brand-name">Neuroscience<br>Research</span></div>
  <nav class="abs nav"><a href="#">Home</a><a href="#">About</a><a href="#">Research</a><a href="#">People</a><a href="#">News / Event</a><a href="#">Contact</a></nav>
  <a class="abs btn-outline">Publications</a>
  <h1 class="abs page-title">Our People</h1>
  <div class="abs title-rule"></div>
</header>

<section class="abs person" style="top:214px;height:210px">
  <div class="portrait warm" style="top:26px" role="img" aria-label="Portrait photo of Tomas Verhaal"></div>
  <div class="name" style="top:47px">Tomas Verhaal</div>
  <div class="role" style="top:63px">Arden Professor of Neuroscience, Halbrook School of Medicine</div>
  <div class="contact" style="top:76px">P. 555 - 014 - 2276 &nbsp;/ &nbsp;E: office@pellorylab.example</div>
  <p class="bio" style="top:105px">It is a long established fact that a reader will be distracted by the readable content of a page when looking at its layout. The point of using Lorem Ipsum is that it has a more-or-less normal distribution of letters, as opposed to using 'Content here, content here', making it look like readable English. Many desktop publishing packages and web page editors now use Lorem Ipsum as their default model text, and a search for 'lorem ipsum' will uncover many web sites infancy.</p>
  <span class="icon-btn solid" style="top:50px" aria-label="Profile link"></span>
  <span class="icon-btn ring" style="top:75px" aria-label="CV document"><svg width="8" height="9" viewBox="0 0 8 9"><path d="M1 .5h4l2 2v6H1z" fill="none" stroke="#2f8ad9" stroke-width=".8"/><path d="M2.3 4.5h3.4M2.3 6h3.4" stroke="#2f8ad9" stroke-width=".6"/></svg></span>
</section>

<section class="abs person alt" style="top:424px;height:228px">
  <div class="portrait dark" style="top:36px" role="img" aria-label="Portrait photo of Ilsa Brannock"></div>
  <div class="name" style="top:57px">Ilsa Brannock</div>
  <div class="role" style="top:73px">Arden Professor of Neuroscience, Halbrook School of Medicine</div>
  <div class="contact" style="top:86px">P. 555 - 014 - 2276 &nbsp;/ &nbsp;E: office@pellorylab.example</div>
  <p class="bio" style="top:115px">It is a long established fact that a reader will be distracted by the readable content of a page when looking at its layout. The point of using Lorem Ipsum is that it has a more-or-less normal distribution of letters, as opposed to using 'Content here, content here', making it look like readable English. Many desktop publishing packages and web page editors now use Lorem Ipsum as their default model text, and a search for 'lorem ipsum' will uncover many web sites infancy.</p>
  <span class="icon-btn solid" style="top:60px" aria-label="Profile link"></span>
  <span class="icon-btn ring" style="top:85px" aria-label="CV document"><svg width="8" height="9" viewBox="0 0 8 9"><path d="M1 .5h4l2 2v6H1z" fill="none" stroke="#2f8ad9" stroke-width=".8"/><path d="M2.3 4.5h3.4M2.3 6h3.4" stroke="#2f8ad9" stroke-width=".6"/></svg></span>
</section>

<section class="abs person" style="top:652px;height:220px">
  <div class="portrait grey" style="top:36px" role="img" aria-label="Portrait photo of Corwin Ashdale"></div>
  <div class="name" style="top:57px">Corwin Ashdale</div>
  <div class="role" style="top:73px">Arden Professor of Neuroscience, Halbrook School of Medicine</div>
  <div class="contact" style="top:86px">P. 555 - 014 - 2276 &nbsp;/ &nbsp;E: office@pellorylab.example</div>
  <p class="bio" style="top:115px">It is a long established fact that a reader will be distracted by the readable content of a page when looking at its layout. The point of using Lorem Ipsum is that it has a more-or-less normal distribution of letters, as opposed to using 'Content here, content here', making it look like readable English. Many desktop publishing packages and web page editors now use Lorem Ipsum as their default model text, and a search for 'lorem ipsum' will uncover many web sites infancy.</p>
  <span class="icon-btn solid" style="top:60px" aria-label="Profile link"></span>
  <span class="icon-btn ring" style="top:85px" aria-label="CV document"><svg width="8" height="9" viewBox="0 0 8 9"><path d="M1 .5h4l2 2v6H1z" fill="none" stroke="#2f8ad9" stroke-width=".8"/><path d="M2.3 4.5h3.4M2.3 6h3.4" stroke="#2f8ad9" stroke-width=".6"/></svg></span>
</section>

<section class="abs cta">
  <h2>Peer-reviewed publications</h2>
  <p>Lorem Ipsum is simply dummy text of the printing and typesetting industry.</p>
  <a class="abs btn-outline">Latest Publications</a>
</section>

<footer class="abs footer">
  <div class="abs brand"><span class="brand-dot"></span><span class="brand-name">Neuroscience<br>Research</span></div>
  <div class="abs footer-rule"></div>
  <div class="abs footer-art" role="img" aria-label="Faint decorative envelope illustration"></div>
  <div class="abs quick">
    <h4>Quick Link</h4>
    <a href="#">About</a><a href="#">Research</a><a href="#">People</a><a href="#">News / Event</a><a href="#">Contact</a>
  </div>
  <div class="abs call">
    <div class="phone">Call. 1-555-010-4567</div>
    <div class="mail">e. hello@pellorylab.example</div>
    <div class="hours">MON - SAT: 8AM TO 8PM SUN: CLOSE</div>
  </div>
  <div class="abs socials"><span aria-label="Social link"></span><span aria-label="Social link"></span><span aria-label="Social link"></span><span aria-label="Social link"></span></div>
  <div class="abs bottom-rule"></div>
  <div class="abs copy">© 2019 Neuroscience Research. All Rights Reserved.</div>
</footer>

</body>
</html>
```